Veltrano - Mechanic/Collision Center Business Card

We're looking for a business card design for our mechanic/ collision repair shop.

Can be with colours or monochromatic.

See the attached files.

Many thanks

```html
<!DOCTYPE html>
<html lang="pt">
<head>
<meta charset="utf-8">
<title>Veltrano – Business Card</title>
<link href="https://fonts.googleapis.com/css2?family=Open+Sans:wght@400;600;700&display=swap" rel="stylesheet">
<style>
  :root {
    --stage: #d9d9d9;
    --card: #2b2b2b;
    --ink: #e9e9e9;
    --ink-soft: #cfcfcf;
    --accent: #2a9fe0;
    --rule: #f2f2f2;
  }
  * { margin: 0; padding: 0; box-sizing: border-box; }
  html, body { width: 1200px; height: 1021px; overflow: hidden; }
  body {
    background: var(--stage);
    font-family: "Open Sans", sans-serif;
    position: relative;
  }
  .card {
    position: absolute;
    background: var(--card);
    box-shadow: 0 6px 18px rgba(0,0,0,.25);
  }
  /* Front */
  .card-front { left: 70px; top: 339px; width: 600px; height: 343px; }
  .front-brand {
    position: absolute; left: 0; right: 0; top: 128px;
    display: flex; align-items: center; justify-content: center; gap: 18px;
  }
  .brand-dot { width: 26px; height: 26px; border-radius: 50%; background: var(--accent); }
  .brand-name {
    color: var(--ink); font-weight: 700; font-size: 52px; letter-spacing: 3px;
    text-transform: uppercase; line-height: 1;
  }
  .front-est {
    position: absolute; left: 0; right: 0; top: 196px; text-align: center;
    color: var(--ink-soft); font-size: 13px; font-weight: 600; letter-spacing: 2px;
  }
  /* Back */
  .card-back { left: 760px; top: 211px; width: 343px; height: 600px; }
  .back-brand {
    position: absolute; left: 0; right: 0; top: 70px;
    display: flex; align-items: center; justify-content: center; gap: 12px;
  }
  .back-brand .brand-dot { width: 18px; height: 18px; }
  .back-brand .brand-name { font-size: 36px; letter-spacing: 2px; }
  .back-est {
    position: absolute; left: 0; right: 0; top: 118px; text-align: center;
    color: var(--ink-soft); font-size: 11px; font-weight: 600; letter-spacing: 2px;
  }
  .person { position: absolute; left: 0; right: 0; top: 220px; text-align: center; }
  .person-name { color: var(--accent); font-size: 24px; text-transform: uppercase; letter-spacing: .5px; }
  .person-role { color: var(--ink); font-size: 15px; text-transform: uppercase; margin-top: 2px; }
  .address {
    position: absolute; left: 0; right: 0; top: 330px; text-align: center;
    color: var(--ink); font-size: 16px; line-height: 1.4;
  }
  .contact-icons {
    position: absolute; left: 0; right: 0; top: 418px;
    display: flex; justify-content: center; gap: 14px;
  }
  .contact-icons svg { width: 16px; height: 16px; }
  .contacts {
    position: absolute; left: 0; right: 0; top: 446px; text-align: center;
    color: var(--ink); font-size: 16px; line-height: 1.45;
  }
</style>
</head>
<body>
  <section class="card card-front" aria-label="Card front">
    <div class="front-brand">
      <span class="brand-dot"></span>
      <span class="brand-name">Veltrano</span>
    </div>
    <p class="front-est">EST. 1979</p>
  </section>

  <section class="card card-back" aria-label="Card back">
    <div class="back-brand">
      <span class="brand-dot"></span>
      <span class="brand-name">Veltrano</span>
    </div>
    <p class="back-est">EST. 1979</p>

    <div class="person">
      <p class="person-name">Rui Marques</p>
      <p class="person-role">Manager</p>
    </div>

    <p class="address">Veltrano, LDA<br>Rua das Oficinas, 42<br>1900-118 Lisboa</p>

    <div class="contact-icons">
      <svg viewBox="0 0 16 16" aria-label="Phone"><path d="M4 1.5l2 3-1.3 1.3a9 9 0 0 0 5.5 5.5L11.5 10l3 2-1.4 2.5C7 14 2 9 1.5 2.9z" fill="var(--accent)"/></svg>
      <svg viewBox="0 0 16 16" aria-label="Mobile"><rect x="4.5" y="1.5" width="7" height="13" rx="1.2" fill="none" stroke="var(--accent)" stroke-width="1.4"/></svg>
      <svg viewBox="0 0 16 16" aria-label="Email"><rect x="1.5" y="3.5" width="13" height="9" fill="none" stroke="var(--accent)" stroke-width="1.4"/><path d="M1.5 3.5l6.5 5 6.5-5" fill="none" stroke="var(--accent)" stroke-width="1.4"/></svg>
      <svg viewBox="0 0 16 16" aria-label="Website"><circle cx="8" cy="8" r="6.5" fill="var(--accent)"/></svg>
    </div>

    <p class="contacts">+351 214550192<br>+351 916204587<br>oficina@veltrano.pt<br>www.veltrano.pt/oficina</p>
  </section>
</body>
</html>
```